Real Estate Managemene Company Needs Business Card Design

We have a logo design and just need business cards made now for our business. Please use PDF logo # 3.

Card with Information to be attached shortly.

The card is used for a real estate management company. We will need to add four other employees and their cards.

Industry/Entity Type

Real Estate

Contact Information for Business Card

Tariq Hamdan
President
3187 Thornwick Avenue
Suite C
Glendale Heights, IL 60152
Phone 630.417.2286
Fax 630.417.2287
Cell 630.473.8062
vantorp@mailbreeze.net

Once design is approved we will have four other employees
Omar Hamdan
Operations Manager

Nadia Hamdan
Administrative Manager

Faz Hamdan
Principal

We would need to take out the cell # 630.473.8062 out for the remaining three cards.

Requirements
Must have
• Please use logo attached

```html
<!DOCTYPE html>
<html lang="en">
<head>
<meta charset="utf-8">
<title>Business Card – Tariq Hamdan</title>
<link href="https://fonts.googleapis.com/css2?family=Montserrat:wght@800&family=Roboto:wght@500&family=Roboto+Slab:wght@400&display=swap" rel="stylesheet">
<style>
  :root {
    --backdrop: #e9e7e4;
    --card-white: #f1f1f1;
    --card-black: #1d1d1d;
    --panel-black: #141414;
    --bar-grey: #5c5c5c;
    --accent-red: #e0232b;
    --accent-red-dark: #a5161c;
    --text-light: #ffffff;
    --icon-dark: #2a2a2a;
  }
  * { margin: 0; padding: 0; box-sizing: border-box; }
  html, body { width: 1200px; height: 1000px; overflow: hidden; }
  body { background: var(--backdrop); position: relative; }

  .business-card {
    position: absolute; left: 100px; top: 215px;
    width: 1000px; height: 570px;
    background: var(--card-black);
    overflow: hidden;
    box-shadow: 0 10px 30px rgba(0,0,0,.18);
  }
  .brand-side {
    position: absolute; left: 0; top: 0; width: 380px; height: 100%;
    background: var(--card-white);
    display: flex; flex-direction: column; align-items: center; justify-content: center;
    gap: 18px; padding: 0 30px;
  }
  .brand-mark { width: 48px; height: 48px; background: var(--accent-red); }
  .brand-name {
    font-family: "Montserrat", sans-serif; font-weight: 800;
    color: var(--accent-red); font-size: 24px; line-height: 1.2;
    text-align: center; text-transform: uppercase;
  }
  .accent-band {
    position: absolute; left: 380px; top: 0; width: 85px; height: 100%;
    background: var(--accent-red);
  }
  .band-fold { position: absolute; left: 380px; width: 50px; height: 100%; top: 0; }

  .identity { position: absolute; left: 495px; top: 78px; color: var(--text-light); }
  .person-name {
    font-family: "Roboto Slab", serif; font-weight: 400;
    font-size: 32px; letter-spacing: 1.5px; text-transform: uppercase; line-height: 1.2;
  }
  .person-title { font-family: "Roboto", sans-serif; font-weight: 500; font-size: 16px; margin-top: 4px; }

  .contact-panel {
    position: absolute; left: 430px; top: 165px; width: 570px; height: 270px;
    background: var(--panel-black);
  }
  .contact-row {
    position: absolute; left: 0; right: 0;
    background: var(--bar-grey);
    display: flex; align-items: center; gap: 22px; padding-left: 40px;
    color: var(--text-light); font-family: "Roboto Slab", serif; font-weight: 400;
  }
  .row-phone { top: 10px; height: 78px; font-size: 16px; line-height: 1.25; }
  .row-email { top: 100px; height: 70px; font-size: 22px; }
  .row-address { top: 182px; height: 80px; font-size: 17px; line-height: 1.25; }
  .contact-icon {
    width: 44px; height: 44px; border-radius: 50%; flex: none;
    background: var(--icon-dark); display: flex; align-items: center; justify-content: center;
  }
  .contact-icon.icon-pin { background: var(--accent-red); }
  .contact-icon svg { width: 22px; height: 22px; }
</style>
</head>
<body>
  <div class="business-card">
    <div class="brand-side">
      <div class="brand-mark"></div>
      <div class="brand-name">Harborview Property<br>Management</div>
    </div>

    <div class="accent-band"></div>
    <svg class="band-fold" viewBox="0 0 50 570" preserveAspectRatio="none" aria-hidden="true">
      <polygon points="20,135 50,165 20,165" fill="var(--accent-red-dark)"/>
      <polygon points="20,435 50,435 20,465" fill="var(--accent-red-dark)"/>
    </svg>

    <div class="identity">
      <div class="person-name">Tariq Hamdan</div>
      <div class="person-title">President</div>
    </div>

    <div class="contact-panel">
      <div class="contact-row row-phone">
        <span class="contact-icon">
          <svg viewBox="0 0 24 24"><path fill="#fff" d="M6.6 10.8a15.1 15.1 0 0 0 6.6 6.6l2.2-2.2a1 1 0 0 1 1-.25 11.4 11.4 0 0 0 3.6.57 1 1 0 0 1 1 1V20a1 1 0 0 1-1 1A17 17 0 0 1 3 4a1 1 0 0 1 1-1h3.5a1 1 0 0 1 1 1c0 1.25.2 2.45.57 3.57a1 1 0 0 1-.25 1z"/></svg>
        </span>
        <div>541.417.2286<br>541.473.8062<br>541.417.2287</div>
      </div>
      <div class="contact-row row-email">
        <span class="contact-icon">
          <svg viewBox="0 0 24 24"><path fill="#fff" d="M2 11 22 3l-6 18-4-7-10-3zm10 3 1 5 3-11z"/></svg>
        </span>
        <div>vantorp@mailbreeze.net</div>
      </div>
      <div class="contact-row row-address">
        <span class="contact-icon icon-pin">
          <svg viewBox="0 0 24 24"><path fill="#fff" d="M12 2a7 7 0 0 0-7 7c0 5 7 13 7 13s7-8 7-13a7 7 0 0 0-7-7zm0 9.5A2.5 2.5 0 1 1 12 6.5a2.5 2.5 0 0 1 0 5z"/></svg>
        </span>
        <div>3187 Thornwick Avenue<br>Suite C<br>Maple Hollow, OR 97152</div>
      </div>
    </div>
  </div>
</body>
</html>
```